Lunaform website scandinavian interior design

Existing website: http://lunaform-example.no/

Webdesign for interior designer Ragna Tveitmo. The company name is Lunaform. Scandinavian interiør is known to be simple and elegant. The website will be in Norwegian, we are working on the text. The website needs to have a few more pages than just the front page. Here are the different titles of the pages:

1. Hjem
2. Om Lunaform
3. Tjenester og priser
4.. Kontakt oss

There should be Chatterloop and Pixelane icons somewhere at the bottom of the website.

The logo we want to use is attached (pink with black print, see attachment )

We have attached images for inspiration. We want to use some of these colors. The color in the logo, The style should be elegant, modern and delicate.

It is imprtant that the website is user friendly.

Target Market(s)

People who want to decorate their home
Companies and public sector who need to redecorate

Industry/Entity Type

Interior Designer

Coding

Coded - Design and coding required

Number of Pages Required

5+ page

Font styles to use
Other font styles liked:
• see example in the logo breakdown

Requirements
Must have
• Elegant, modern and delicate design
Images of design, see examples attached
Colors similar to the pictures
Should not have
• Too bright colors
Pictures of people

```html
<!DOCTYPE html>
<html lang="en">
<head>
<meta charset="utf-8">
<title>Lunaform – Interior Design</title>
<link href="https://fonts.googleapis.com/css2?family=Mulish:wght@300;400;600&display=swap" rel="stylesheet">
<style>
  :root {
    --blush: #ead3c9;
    --blush-soft: #efdcd3;
    --espresso: #231210;
    --ink: #2a1a17;
    --muted: #6d605c;
    --white: #ffffff;
    --rule: #cbb9b2;
  }
  * { margin: 0; padding: 0; box-sizing: border-box; }
  html, body { width: 687px; height: 1200px; overflow: hidden; }
  body {
    position: relative;
    background: var(--white);
    font-family: "Mulish", sans-serif;
    color: var(--ink);
  }
  .abs { position: absolute; }

  /* Header */
  .site-header {
    position: absolute; left: 0; top: 0; width: 687px; height: 120px;
    background: linear-gradient(to bottom, var(--blush) 0%, var(--blush) 70%, #f6ebe6 100%);
  }
  .nav-link {
    position: absolute; top: 42px; font-size: 6.2px; letter-spacing: 0.1px;
    color: var(--ink); text-transform: uppercase;
  }
  .nav-link.active { border-bottom: 0.8px solid var(--ink); padding-bottom: 1.5px; }
  .nav-sep { position: absolute; top: 41px; font-size: 6.5px; color: var(--ink); }
  .brand {
    position: absolute; left: 283px; top: 28px; width: 120px;
    display: flex; align-items: center; justify-content: center; gap: 5px;
    font-size: 19px; font-weight: 400; color: var(--espresso); letter-spacing: 0.3px;
  }
  .brand-mark { width: 7px; height: 7px; border: 0.8px solid var(--espresso); }

  /* Hero */
  .hero-photo {
    left: 25px; top: 91px; width: 641px; height: 270px;
    background: linear-gradient(160deg, #efe9e2 0%, #d9cbbb 30%, #b8895a 55%, #e4dcd3 72%, #4e6f7c 100%);
  }
  .hero-panel {
    left: 404px; top: 138px; width: 216px; height: 137px;
    background: rgba(255,255,255,0.86);
  }
  .hero-title {
    position: absolute; right: 13px; top: 15px; text-align: right;
    font-size: 17px; line-height: 26px; color: var(--espresso); font-weight: 400;
  }
  .hero-title strong { font-weight: 600; letter-spacing: -0.3px; }
  .btn-dark {
    position: absolute; background: var(--espresso); color: var(--white);
    font-size: 5.6px; text-transform: uppercase; display: flex;
    align-items: center; justify-content: center; letter-spacing: 0.1px;
  }
  .hero-cta { left: 121px; top: 94px; width: 80px; height: 25px; }

  /* About */
  .section-title { font-size: 17px; line-height: 20.5px; font-weight: 400; color: var(--espresso); }
  .about-title { left: 134px; top: 416px; }
  .title-rule { height: 1px; width: 29px; }
  .about-rule { left: 134px; top: 471px; background: var(--rule); }
  .about-copy {
    left: 134px; top: 486px; width: 192px;
    font-size: 5.6px; line-height: 12.3px; color: var(--muted); font-weight: 400;
  }
  .about-cta { left: 134px; top: 585px; width: 105px; height: 25px; }
  .about-photo {
    left: 361px; top: 408px; width: 191px; height: 214px;
    background: linear-gradient(170deg, #f1f1ef 0%, #d6d5d1 45%, #7c7c78 70%, #2f3a34 88%, #c9a43e 100%);
  }

  /* Services */
  .services-band { left: 0; top: 658px; width: 687px; height: 387px; background: var(--blush-soft); }
  .services-title { left: 134px; top: 694px; }
  .services-rule { left: 134px; top: 728px; background: var(--espresso); height: 1.2px; }
  .btn-outline {
    left: 470px; top: 694px; width: 83px; height: 25px;
    border: 0.7px solid var(--espresso); color: var(--espresso);
    font-size: 5.4px; line-height: 8.5px; text-align: center; text-transform: uppercase;
    display: flex; align-items: center; justify-content: center;
  }
  .service-card { top: 748px; width: 203px; height: 261px; overflow: hidden; }
  .service-card .card-photo { position: absolute; inset: 0; }
  .service-card .card-label {
    position: absolute; left: 0; bottom: 0; width: 100%; height: 34px;
    background: rgba(255,255,255,0.9); padding-left: 11px;
    font-size: 12px; line-height: 34px; color: var(--espresso);
  }
  .card-private { left: 25px; }
  .card-private .card-photo { background: linear-gradient(120deg, #e9ebe9 0%, #9fb27a 40%, #f2f0ec 65%, #7a6252 100%); }
  .card-corporate { left: 244px; }
  .card-corporate .card-photo { background: linear-gradient(180deg, #4a4a48 0%, #7d8a4c 25%, #b07a47 55%, #d2c3ac 80%, #e9e6e1 100%); }
  .card-public { left: 463px; }
  .card-public .card-photo { background: linear-gradient(180deg, #a9b5bb 0%, #e4e6e4 45%, #3b3632 70%, #f1f1ef 100%); }

  /* Footer */
  .footer-link { position: absolute; top: 1080px; font-size: 6.3px; color: var(--ink); }
  .footer-sep { position: absolute; top: 1079px; font-size: 6.3px; color: var(--ink); }
  .footer-info {
    left: 0; top: 1097px; width: 687px; text-align: center;
    font-size: 6.1px; color: var(--ink); word-spacing: 0.5px;
  }
  .footer-info .sep { margin: 0 6px; }
  .social {
    left: 0; top: 1117px; width: 687px; display: flex; justify-content: center; gap: 12px;
    font-size: 6.3px; color: var(--ink);
  }
  .social-item { display: flex; align-items: center; gap: 4px; }
  .social-dot { width: 12px; height: 12px; border-radius: 50%; }
  .dot-chatterloop { background: #34509a; }
  .dot-pixelane { background: #5a2f26; }
  .legal-bar {
    left: 0; top: 1168px; width: 687px; height: 32px; background: var(--espresso);
    color: var(--white); font-size: 6px; text-align: center; line-height: 32px;
  }
</style>
</head>
<body>

<header class="site-header">
  <a class="nav-link active" style="left:164px">Home</a>
  <span class="nav-sep" style="left:203px">|</span>
  <a class="nav-link" style="left:226px">About Lunaform</a>
  <div class="brand"><span class="brand-mark"></span>Lunaform</div>
  <a class="nav-link" style="left:413px">Services &amp; Prices</a>
  <span class="nav-sep" style="left:488px">|</span>
  <a class="nav-link" style="left:511px">Contact Us</a>
</header>

<section>
  <div class="abs hero-photo" role="img" aria-label="Bright open-plan living room and kitchen with cream sofas, patterned cushions, pendant lamps and a chandelier"></div>
  <div class="abs hero-panel">
    <h1 class="hero-title">NEED HELP<br><strong>DEVELOPING INTERIOR</strong><br>ENVIRONMENTS ?</h1>
    <a class="btn-dark hero-cta">Contact Us</a>
  </div>
</section>

<section>
  <h2 class="abs section-title about-title">We Are The Leader In<br>The Interior Design</h2>
  <div class="abs title-rule about-rule"></div>
  <p class="abs about-copy">Company Lunaform AS is working on the development of interior environments for private, corporate and public institutions. Finding the optimal solutions for a project, whether it is a room or more, requires knowledge and knowledge in the market. Using professional expertise in the field will save you both time and money.<br>Using floor plans / furniture plans, 3D drawings, collages or "make a living collage" - we find the best solutions for you as a customer.</p>
  <a class="btn-dark about-cta">Read More About Us</a>
  <div class="abs about-photo" role="img" aria-label="Modern grey living room with velvet cushions, framed art and a view to a dining area"></div>
</section>

<section>
  <div class="abs services-band"></div>
  <h2 class="abs section-title services-title">Our Services &amp; Prices</h2>
  <div class="abs title-rule services-rule"></div>
  <a class="abs btn-outline">View More<br>Services &amp; Prices</a>

  <article class="abs service-card card-private">
    <div class="card-photo" role="img" aria-label="Marble bathroom with a freestanding bathtub beside large windows and plants"></div>
    <div class="card-label">Private Interior</div>
  </article>
  <article class="abs service-card card-corporate">
    <div class="card-photo" role="img" aria-label="Industrial office with hanging greenery, wooden slat ceiling and desks"></div>
    <div class="card-label">Corporate Interior</div>
  </article>
  <article class="abs service-card card-public">
    <div class="card-photo" role="img" aria-label="Gallery hall with a bronze statue on a plinth and framed paintings"></div>
    <div class="card-label">Public Interior</div>
  </article>
</section>

<footer>
  <a class="footer-link" style="left:207px">Home</a>
  <span class="footer-sep" style="left:246px">|</span>
  <a class="footer-link" style="left:269px">About Lunaform</a>
  <span class="footer-sep" style="left:332px">|</span>
  <a class="footer-link" style="left:355px">Services &amp; Prices</a>
  <span class="footer-sep" style="left:423px">|</span>
  <a class="footer-link" style="left:446px">Contact Us</a>

  <p class="abs footer-info">Lunaform AS v / Ragna Tveitmo&nbsp; Skjærgårdsveien 14&nbsp; 3190 Nordvika<span class="sep">|</span>Tel. +4740012345<span class="sep">|</span>Mail. post@lunaform-example.no<span class="sep">|</span>Web. www.lunaform-example.no</p>

  <div class="abs social">
    <a class="social-item"><span class="social-dot dot-chatterloop"></span>Chatterloop</a>
    <a class="social-item"><span class="social-dot dot-pixelane"></span>Pixelane</a>
  </div>

  <div class="abs legal-bar">© 2020&nbsp; Lunaform. All Rights Reserved.</div>
</footer>

</body>
</html>
```